Termite Mailer September 2021

We need a clean modern looking flyer advertising termites via the mail.

Size should be 9"x6"

Our tagline is "The Smarter Approach to Pest Control"

Something along the stylistic design of these:

https://pics.snapvault.example/Kq73rTbWm2ZxLp9h4

https://pics.snapvault.example/8RvNcYdHq4TkWsuj2

https://pics.snapvault.example/mH2QxGzLp739jVcbD

https://www.flyerkrafthub.com/wp-content/uploads/designs/img/Pest-Prevention-Postcard-PST-1003.jpg

Should include some of this verbiage:

HAVE YOU SCHEDULED YOUR ANNUAL TERMITE INSPECTION? - MAKE IT IN RED

DON'T WAIT. PROTECT YOUR HOME TODAY!

ABSOLUTELY FREE INSPECTION. NO OBLIGATION.

TERMITES CAN CAUSE SEVERE DAMAGE TO YOUR HOME.

BRELLANOVA LOGO

THE SMARTER APPROACH TO PEST CONTROL.

PROTECT YOUR MOST VALUABLE ASSET.

10% DISCOUNT ON ANY SERVICE GUARANTEED IF YOU CALL TODAY.

INCLUDE A PICTURE OF A TERMITE AS WELL SOMEWHERE AND WOOD DAMAGE.

Target Market(s)

Homeowners in Southern California USA

Industry/Entity Type

Pest Control/Extermination

Font styles to use
Other font styles liked:
• Chaparral Pro Italic, Brava Slab

Requirements
Must have
• Clean design, picture of house, picture of Termite, 10% off coupon and call to action on the back
Should not have
• Bad looking houses, colors that don't match our logo

```html
<!DOCTYPE html>
<html lang="en">
<head>
<meta charset="utf-8">
<title>BRELLANOVA Termite Mailer</title>
<link href="https://fonts.googleapis.com/css2?family=Zilla+Slab:ital,wght@0,500;0,700;1,600&family=Bree+Serif&family=Arimo:wght@400;700&display=swap" rel="stylesheet">
<style>
  :root {
    --bg: #e8e8e8;
    --green: #7dc24a;
    --blue: #0b72b9;
    --red: #c1272d;
    --ink: #1a1a1a;
    --panel: #f3f4f6;
    --white: #ffffff;
  }
  * { margin: 0; padding: 0; box-sizing: border-box; }
  html, body { width: 800px; height: 1200px; overflow: hidden; }
  body { background: var(--bg); position: relative; font-family: "Zilla Slab", serif; color: var(--ink); }

  .card {
    position: absolute; left: 67px; width: 666px; height: 445px;
    background: var(--white); overflow: hidden;
    box-shadow: 3px 3px 0 #c4c4c4;
  }
  .card--front { top: 116px; }
  .card--back { top: 634px; }

  .shapes { position: absolute; inset: 0; }

  .band {
    position: absolute; left: 0; top: 0; width: 100%; height: 78px;
    background: var(--green);
  }
  .band__title {
    position: absolute; left: 16px; top: 20px;
    font-weight: 700; font-size: 31px; color: var(--white);
    letter-spacing: -0.2px; transform: scaleX(0.92); transform-origin: left;
    white-space: nowrap;
  }
  .band__title--two-line {
    left: 19px; top: 12px; font-size: 27px; line-height: 31px;
  }

  .headline {
    position: absolute; left: 15px; top: 95px;
    font-weight: 700; font-size: 25.5px; line-height: 30px; color: var(--red);
    transform: scaleX(0.92); transform-origin: left; white-space: nowrap;
  }
  .subhead {
    position: absolute; left: 15px; top: 165px;
    font-style: italic; font-weight: 600; font-size: 23px; line-height: 28px;
    transform: scaleX(0.92); transform-origin: left; white-space: nowrap;
  }

  .badge {
    position: absolute; width: 118px; height: 118px; border-radius: 50%;
    background: var(--green);
    box-shadow: 0 6px 6px -3px rgba(0,0,0,0.18);
    display: flex; flex-direction: column; align-items: center; justify-content: center;
    color: var(--white); text-align: center; text-transform: uppercase;
  }
  .badge::before {
    content: ""; position: absolute; inset: 4px; border-radius: 50%;
    border: 1.5px dashed var(--white);
  }
  .badge--free { left: 14px; top: 234px; }
  .badge--discount { left: 147px; top: 232px; }
  .badge__strong { font-weight: 700; font-size: 13px; line-height: 15px; }
  .badge__big { font-weight: 700; font-size: 22px; line-height: 20px; }
  .badge__text { font-weight: 500; font-size: 10.5px; line-height: 13px; }
  .badge__small { font-weight: 500; font-size: 8px; line-height: 12px; }

  .cta {
    position: absolute; left: 16px; top: 369px; color: var(--white);
    font-family: "Bree Serif", serif;
  }
  .cta__lead { font-size: 15px; line-height: 18px; }
  .cta__row { display: flex; align-items: center; gap: 5px; margin-top: 5px; }
  .cta__phone { font-family: "Arimo", sans-serif; font-size: 17.5px; }
  .cta__web { font-size: 10px; margin-left: 7px; }
  .cta__icon { width: 18px; height: 18px; flex: none; }

  .brand {
    position: absolute; left: 372px; top: 382px;
    display: flex; align-items: center; gap: 10px;
  }
  .brand__mark { width: 44px; height: 44px; border-radius: 50%; background: var(--green); }
  .brand__name {
    font-weight: 700; font-size: 35px; color: var(--blue); letter-spacing: 0.5px;
  }

  .mail-panel {
    position: absolute; left: 20px; top: 114px;
    font-style: italic; font-weight: 600; font-size: 20px; line-height: 25px;
    transform: scaleX(0.93); transform-origin: left;
  }
  .mail-panel p + p { margin-top: 14px; }
  .offer { position: absolute; left: 15px; top: 242px; }
  .offer__big {
    font-weight: 700; font-size: 42px; line-height: 46px; color: var(--red);
    transform: scaleX(0.92); transform-origin: left; white-space: nowrap;
  }
  .offer__text {
    font-weight: 500; font-size: 19.5px; line-height: 26px;
    transform: scaleX(0.92); transform-origin: left; white-space: nowrap;
  }

  .address-box {
    position: absolute; left: 415px; top: 15px; width: 157px; height: 51px;
    background: var(--white); border: 1px solid #333;
    font-family: "Arimo", sans-serif; color: #111;
  }
  .address-box__code { position: absolute; top: 6px; width: 100%; text-align: center; font-size: 7px; }
  .address-box__to { position: absolute; left: 11px; top: 27px; font-size: 7.5px; font-weight: 700; line-height: 10px; }
  .indicia {
    position: absolute; left: 589px; top: 15px; width: 69px; height: 51px;
    background: var(--white); border: 1px solid #333;
    font-family: "Arimo", sans-serif; font-size: 7.5px; line-height: 9.6px;
    text-align: center; color: #111; padding-top: 1px;
  }
  .indicia strong { font-size: 9px; }
  .address-line {
    position: absolute; left: 380px; width: 278px;
    border-top: 1px dotted #8a8a8a;
  }
</style>
</head>
<body>

  <!-- Front -->
  <section class="card card--front">
    <svg class="shapes" width="666" height="445" viewBox="0 0 666 445">
      <defs>
        <linearGradient id="homeTones" x1="0" y1="0" x2="0" y2="1">
          <stop offset="0" stop-color="#dfe6ec"/>
          <stop offset="0.55" stop-color="#c9ced1"/>
          <stop offset="1" stop-color="#4c7a36"/>
        </linearGradient>
        <linearGradient id="termiteTones" x1="0" y1="0" x2="1" y2="1">
          <stop offset="0" stop-color="#5a3b22"/>
          <stop offset="0.5" stop-color="#b27a36"/>
          <stop offset="1" stop-color="#6e4c2c"/>
        </linearGradient>
        <radialGradient id="antTones" cx="0.55" cy="0.5" r="0.55">
          <stop offset="0" stop-color="#2a2526"/>
          <stop offset="0.6" stop-color="#6b6567"/>
          <stop offset="1" stop-color="#ffffff" stop-opacity="0"/>
        </radialGradient>
      </defs>
      <polygon points="0,78 443,78 274,362 0,362" fill="var(--panel)"/>
      <polygon role="img" aria-label="Photo of a smiling family standing in front of a clean white house" points="443,84 666,84 666,240 354,240" fill="url(#homeTones)"/>
      <rect role="img" aria-label="Photo of a large black ant" x="255" y="250" width="210" height="112" rx="40" fill="url(#antTones)"/>
      <polygon role="img" aria-label="Close-up photo of termites on damaged wood" points="518,247 666,247 666,354 450,354" fill="url(#termiteTones)"/>
      <polygon points="0,362 274,362 322,445 0,445" fill="var(--blue)"/>
      <polygon points="274,362 280,362 328,445 322,445" fill="var(--green)"/>
    </svg>

    <div class="band"><h1 class="band__title">THE SMARTER APPROACH TO PEST CONTROL</h1></div>

    <h2 class="headline">HAVE YOU SCHEDULED YOUR<br>ANNUAL TERMITE INSPECTION?</h2>
    <p class="subhead">DON'T WAIT. PROTECT YOUR<br>HOME TODAY!</p>

    <div class="badge badge--free">
      <span class="badge__strong">Absolutely</span>
      <span class="badge__strong">Free</span>
      <span class="badge__text">Inspection.</span>
      <span class="badge__text">No obligation.</span>
    </div>
    <div class="badge badge--discount">
      <span class="badge__big">10%</span>
      <span class="badge__strong">Discount</span>
      <span class="badge__text">On any service</span>
      <span class="badge__text">Guaranteed</span>
      <span class="badge__small">If you call today.</span>
    </div>

    <div class="cta">
      <p class="cta__lead">Call us for an appointment today!</p>
      <div class="cta__row">
        <svg class="cta__icon" viewBox="0 0 20 20"><circle cx="10" cy="10" r="10" fill="var(--green)"/><path d="M6.5 5c.6-.5 1.3-.4 1.6.2l.9 1.8c.2.5 0 1-.4 1.3l-.6.4c.5 1.2 1.5 2.3 2.7 2.9l.5-.6c.3-.4.9-.5 1.3-.3l1.7 1c.5.3.6 1 .2 1.5-.9 1.2-2 1.4-3.4.7-2.3-1.1-4-3-4.9-5.3-.5-1.4-.3-2.8.4-3.6z" fill="#fff"/></svg>
        <span class="cta__phone">+000 1123 4523 0000</span>
      </div>
      <div class="cta__row">
        <svg class="cta__icon" viewBox="0 0 20 20"><circle cx="10" cy="10" r="10" fill="var(--green)"/><circle cx="10" cy="10" r="5" fill="none" stroke="#fff" stroke-width="1.2"/><path d="M5 10h10M10 5c-2 3-2 7 0 10M10 5c2 3 2 7 0 10" fill="none" stroke="#fff" stroke-width="1"/></svg>
        <span class="cta__web">www.youradressgoeshere</span>
      </div>
    </div>

    <div class="brand"><span class="brand__mark"></span><span class="brand__name">BRELLANOVA</span></div>
  </section>

  <!-- Back -->
  <section class="card card--back">
    <svg class="shapes" width="666" height="445" viewBox="0 0 666 445">
      <polygon points="0,85 410,85 278,362 0,362" fill="var(--panel)"/>
      <polygon points="0,362 274,362 322,445 0,445" fill="var(--blue)"/>
      <polygon points="274,362 280,362 328,445 322,445" fill="var(--green)"/>
    </svg>

    <div class="band"><h1 class="band__title band__title--two-line">TERMITES CAN CAUSE SEVERE<br>DAMAGE TO YOUR HOME.</h1></div>

    <div class="address-box">
      <span class="address-box__code">*****************ECRWSS****</span>
      <span class="address-box__to">Local<br>Postal Customer</span>
    </div>
    <div class="indicia">PRSRT STD<br>ECRWSS<br>U.S.POSTAGE<br><strong>PAID</strong><br>EDDM Retail</div>

    <div class="mail-panel">
      <p>THE SMARTER APPROACH TO PEST<br>CONTROL.</p>
      <p>PROTECT YOUR MOST VALUABLE<br>ASSET.</p>
    </div>

    <div class="offer">
      <p class="offer__big">10% DISCOUNT</p>
      <p class="offer__text">ON ANY SERVICE GUARANTEED<br>IF YOU CALL TODAY.</p>
    </div>

    <span class="address-line" style="top:181px"></span>
    <span class="address-line" style="top:228px"></span>
    <span class="address-line" style="top:276px"></span>

    <div class="cta">
      <p class="cta__lead">Call us for an appointment today!</p>
      <div class="cta__row">
        <svg class="cta__icon" viewBox="0 0 20 20"><circle cx="10" cy="10" r="10" fill="var(--green)"/><path d="M6.5 5c.6-.5 1.3-.4 1.6.2l.9 1.8c.2.5 0 1-.4 1.3l-.6.4c.5 1.2 1.5 2.3 2.7 2.9l.5-.6c.3-.4.9-.5 1.3-.3l1.7 1c.5.3.6 1 .2 1.5-.9 1.2-2 1.4-3.4.7-2.3-1.1-4-3-4.9-5.3-.5-1.4-.3-2.8.4-3.6z" fill="#fff"/></svg>
        <span class="cta__phone">+000 1123 4523 0000</span>
      </div>
      <div class="cta__row">
        <svg class="cta__icon" viewBox="0 0 20 20"><circle cx="10" cy="10" r="10" fill="var(--green)"/><circle cx="10" cy="10" r="5" fill="none" stroke="#fff" stroke-width="1.2"/><path d="M5 10h10M10 5c-2 3-2 7 0 10M10 5c2 3 2 7 0 10" fill="none" stroke="#fff" stroke-width="1"/></svg>
        <span class="cta__web">www.youradressgoeshere</span>
      </div>
    </div>

    <div class="brand"><span class="brand__mark"></span><span class="brand__name">BRELLANOVA</span></div>
  </section>

</body>
</html>
```